Food fans website needs a desktop homepage design

We need a desktop homepage design for Zestmora.co.uk, a website to help you to find the best restaurants in each main city of Europe, with initial focus on London. It is not a directory with thousands of restaurants and reviews, else lists of top 20 restaurants for each area of the city. Food fans from all around the city will be able to keep an itinerary of where they eat, showing them later funny stats like "this month you really went for pizzas, don't you?". Keep it funny but professional.

A bit of branding has been done but this project give you total freedom to design the homepage of the site. The design must be a mix between minimal, flat and clean layout. The main idea is to keep it simple, easy to use and showing just the necessary elements.

For the font and colour scheme, we would like to use a thin but energetic font using the #E1393A colour as starting point even if you have freedom to slightly modify it. Blacks, greys and whites can be the secondary colours but we are open to introduce another main colour to the site like green, orange or yellow.

A simple wireframe has been attached to help you but the main elements that the page requires are the next:
- Panoramic fancy image in the header to contain the logo and the search form (the fields of the form are specified on the wireframe) and maybe some animated text to fill the right gap.
- List of results (10 results per page) showing the main info for each restaurant: name, thumbnail, location (zone, area), category, price, description, rating (no with stars please) and whatever you want to add that makes sense.
- Right hand sidebar with 3 widgets: Categories, Location and prices.

You can get the icons from vendrako.net.

We are open to have some text-shadows, rounded corners, box-shadows but trying to keep it minimal, flat and clean as much as possible. The main attractive of the site are the food/restaurant images.

Target Market(s)

22 - 45 food fans lovers from the city. busy people that want to disconnect and relax through the food. The don't mind to pay for quality and new experiences. Up to meet new places around them.

Industry/Entity Type

Restaurant

Requirements
Must have
• Panoramic image in the header, restaurants search form as per wireframe, list results with pagination, right hand sidebar with the widgets mention above and a nice footer with extra elements like "latest restaurants, latest tweets, etc.."
Nice to have
• This site will only be supported by the latest browsers so the idea is to have nice CSS3 transitions all around. Have that in mind at the time to design it even if you cannot show it on the design.
Should not have
• Busy backgrounds and unnecessary images that would slow down the page load.

```html
<!DOCTYPE html>
<html lang="en">
<head>
<meta charset="utf-8">
<title>Zestmora — Food fans in London</title>
<link href="https://fonts.googleapis.com/css2?family=Lato:ital,wght@0,300;0,400;0,700;0,900;1,300;1,400;1,700;1,900&display=swap" rel="stylesheet">
<style>
:root{
  --red:#e1393a;
  --ink:#333333;
  --text:#444444;
  --muted:#777777;
  --line:#d9d9d9;
  --box:#cfcfcf;
  --check:#2fa84f;
  --social:#c8c8c8;
  --white:#ffffff;
}
*{margin:0;padding:0;box-sizing:border-box}
html,body{width:821px;height:1200px;overflow:hidden;background:var(--white)}
body{position:relative;font-family:'Lato',sans-serif;color:var(--text)}
.abs{position:absolute}

/* hero */
.hero{left:0;top:0;width:821px;height:413px;overflow:hidden;
  background:linear-gradient(100deg,#eceef2 0%,#e4e6ea 40%,#d9c7b5 55%,#b5825a 68%,#c88f5f 78%,#e6e2de 92%,#f0f0f2 100%)}
.hero-photo{left:0;top:0;width:821px;height:413px;
  background:radial-gradient(ellipse 180px 150px at 520px 190px,rgba(178,104,60,.85),rgba(178,104,60,0) 70%),
             radial-gradient(ellipse 200px 90px at 640px 330px,rgba(120,70,40,.5),rgba(120,70,40,0) 70%)}
.site-title{left:101px;top:34px;font-size:30px;font-weight:700;color:var(--ink);letter-spacing:-.2px}
.hero-tagline{left:366px;top:228px;font-size:47px;line-height:56px;font-weight:900;font-style:italic;color:var(--white);letter-spacing:-.5px;text-shadow:0 1px 3px rgba(0,0,0,.25)}

.search{left:102px;top:108px;width:214px;height:276px;background:var(--white);border:1px solid #d4d4d4;box-shadow:0 1px 3px rgba(0,0,0,.15);padding:0 0 0 18px}
.search .label{position:absolute;left:18px;font-size:9px;letter-spacing:.6px;color:var(--muted);font-weight:400}
.search .field{position:absolute;left:18px;width:126px;height:21px;border:1px solid var(--line);font-size:8.5px;font-style:italic;color:var(--ink);padding:6px 0 0 6px}
.search .field.active{border:none;border-bottom:1px solid var(--red);width:152px}
.search .from{position:absolute;left:18px;top:198px;font-size:8.5px;color:var(--muted);display:flex;align-items:center;gap:5px}
.select{display:inline-block;width:38px;height:15px;border:1px solid var(--line);font-size:8px;padding:2px 0 0 3px;position:relative;color:#aaa}
.select.on{border-color:var(--red);color:var(--ink)}
.select::after{content:"";position:absolute;right:4px;top:6px;border:3px solid transparent;border-top:3px solid #555}
.btn{position:absolute;left:18px;top:236px;width:58px;height:22px;background:var(--red);color:var(--white);font-size:8.5px;font-weight:700;letter-spacing:.6px;text-align:center;line-height:22px}

/* results */
.divider{left:536px;top:413px;width:1px;height:580px;background:var(--line)}
.results-title{left:101px;top:426px;font-size:37px;font-weight:300;font-style:italic;color:#555;letter-spacing:-.3px}
.results-title em{color:var(--red);font-weight:400}

.listing{left:101px;width:420px;height:140px}
.thumb{position:absolute;left:0;top:0;width:100px;height:100px;border:3px solid #cfcfcf}
.listing .name{position:absolute;left:114px;top:-4px;font-size:23px;font-weight:400;color:var(--ink);white-space:nowrap;display:flex;align-items:center;gap:12px}
.rating{display:inline-flex;gap:3px}
.rating i{width:5px;height:5px;border-radius:50%;background:var(--red);display:block}
.rating i.off{background:#aaa}
.meta{position:absolute;left:114px;font-size:7.6px;color:var(--ink);display:flex;align-items:center;gap:4px;white-space:nowrap}
.meta svg{width:8px;height:8px;fill:#999;flex:none}
.meta .gap{width:10px}
.desc{position:absolute;left:114px;top:88px;width:275px;font-size:7.6px;line-height:10px;color:var(--ink)}
.desc b{font-weight:700}
.desc a,.more{color:var(--red);text-decoration:none}
.sep{left:60px;width:425px;height:0;border-top:2px dotted #d0d0d0}

/* sidebar */
.widget{left:562px}
.widget h3{font-size:15px;font-weight:400;color:var(--ink);letter-spacing:.6px;margin-bottom:11px}
.widget li{list-style:none;font-size:8.4px;color:var(--text);height:19px;display:flex;align-items:center;gap:8px}
.cb{width:8px;height:8px;border:1px solid #bdbdbd;position:relative;flex:none}
.cb svg{position:absolute;left:-1px;top:-3px;width:10px;height:10px}
.widget .more{font-size:8.4px;display:block;margin-top:2px}

/* footer */
.footer-line{left:0;top:993px;width:821px;height:1px;background:var(--line)}
.foot-h{font-size:11px;color:var(--red);font-weight:400}
.newest{left:101px;top:1016px}
.newest li{list-style:none;font-size:7px;color:var(--ink);height:15.2px;margin-top:0}
.newest ul{margin-top:12px}
.tweets{left:265px;top:1016px;width:190px}
.tweet{font-size:7px;line-height:15.5px;color:var(--ink);padding:6px 0 8px;border-bottom:1px solid var(--line);width:96px;white-space:nowrap}
.tweet:last-child{border:none}
.tweets .list{margin-top:4px}
.social{left:505px;top:1040px;display:flex;gap:17px}
.social span{width:40px;height:40px;border-radius:50%;background:var(--social);color:var(--white);font-size:7px;font-weight:700;display:flex;align-items:center;justify-content:center}
.social span.first{background:var(--red)}
.copy{left:505px;top:1111px;font-size:8.4px;line-height:11px;color:var(--ink)}
</style>
</head>
<body>
<svg width="0" height="0" style="position:absolute">
  <symbol id="i-phone" viewBox="0 0 10 10"><path d="M1 3h8v2H7V4H3v1H1zM2 6h6l1 3H1z"/></symbol>
  <symbol id="i-web" viewBox="0 0 10 10"><path d="M0 1h10v6H0zM1 2v4h8V2zM3 8h4v1H3z"/></symbol>
  <symbol id="i-mail" viewBox="0 0 10 10"><path d="M0 2h10v6H0zM1 3l4 3 4-3z"/></symbol>
  <symbol id="i-pin" viewBox="0 0 10 10"><path d="M5 0a3.5 3.5 0 0 1 3.5 3.5C8.5 6 5 10 5 10S1.5 6 1.5 3.5A3.5 3.5 0 0 1 5 0zm0 2a1.5 1.5 0 1 0 0 3 1.5 1.5 0 0 0 0-3z"/></symbol>
  <symbol id="i-fork" viewBox="0 0 10 10"><path d="M1 1l1-1 7 8-1 1zM3 1l.7-.7 2 2-.7.7z"/></symbol>
  <symbol id="i-bag" viewBox="0 0 10 10"><path d="M4 0h2l-.5 2h-1zM3 3h4c1 1 2 3 2 5s-2 2-4 2-4 0-4-2 1-4 2-5z"/></symbol>
  <symbol id="i-tick" viewBox="0 0 10 10"><path d="M1 5l2-1 2 2 4-6 1 1-5 8z" fill="#2fa84f"/></symbol>
</svg>

<header class="abs hero" role="img" aria-label="Photograph of a plated gourmet dish with pastry, seared meat and roasted vegetables on a white plate">
  <div class="abs hero-photo"></div>
</header>
<h1 class="abs site-title">Food fans in London</h1>
<p class="abs hero-tagline">Search the best<br>restaurants.</p>

<form class="abs search">
  <span class="label" style="top:21px">WHAT RESTAURANT</span>
  <span class="field active" style="top:37px">Verano</span>
  <span class="label" style="top:75px">WHAT KIND OF FOOD</span>
  <span class="field" style="top:86px">French</span>
  <span class="label" style="top:129px">WHERE</span>
  <span class="field" style="top:140px">London</span>
  <span class="label" style="top:183px">PRICES</span>
  <span class="from">From <span class="select on">£39</span> To <span class="select">£150</span></span>
  <span class="btn">SEARCH</span>
</form>

<div class="abs divider"></div>
<h2 class="abs results-title">Best restaurants in <em>London</em></h2>

<article class="abs listing" style="top:505px">
  <div class="thumb" role="img" aria-label="Photo of a plated starter with tomato and micro herbs" style="background:linear-gradient(135deg,#f2eeea,#d9544c 55%,#7a3a2a)"></div>
  <h3 class="name">Verano <span class="rating"><i></i><i></i><i></i><i></i><i class="off"></i></span></h3>
  <p class="meta" style="top:27px"><svg><use href="#i-phone"/></svg>020 7946 0123<span class="gap"></span><svg><use href="#i-web"/></svg>Website<span class="gap"></span><svg><use href="#i-mail"/></svg>E-mail</p>
  <p class="meta" style="top:48px"><svg><use href="#i-pin"/></svg>14 Marlow Mews | Knightsbridge, London SW1X 9QT, England (Victoria)</p>
  <p class="meta" style="top:68px"><svg><use href="#i-fork"/></svg>French<span class="gap"></span><svg><use href="#i-bag"/></svg>£20 - £350</p>
  <p class="desc"><b>Description:</b> Renowned throughout London and beyond, Verano is one of the biggest names on the restaurant scene. With the world-renowned Marcus Ellery behind the scheme to raise Verano... <a>more</a></p>
</article>
<div class="abs sep" style="top:641px"></div>

<article class="abs listing" style="top:669px">
  <div class="thumb" role="img" aria-label="Photo of fried fish with chips" style="background:linear-gradient(135deg,#e8b867,#c98a36 60%,#f0e3c8)"></div>
  <h3 class="name">Hadley's Fish and Chips <span class="rating"><i></i><i></i><i></i><i class="off"></i><i class="off"></i></span></h3>
  <p class="meta" style="top:27px"><svg><use href="#i-phone"/></svg>020 7946 0123<span class="gap"></span><svg><use href="#i-web"/></svg>Website<span class="gap"></span><svg><use href="#i-mail"/></svg>E-mail</p>
  <p class="meta" style="top:48px"><svg><use href="#i-pin"/></svg>48 Fenwick Rd, London SW6 4LP, England</p>
  <p class="meta" style="top:68px"><svg><use href="#i-fork"/></svg>English, Hamburgers, British, Fish &amp; Chips</p>
  <p class="meta" style="top:88px"><svg><use href="#i-bag"/></svg>£3 - £11</p>
</article>
<div class="abs sep" style="top:805px"></div>

<article class="abs listing" style="top:833px">
  <div class="thumb" role="img" aria-label="Photo of a salmon dish with herbs and vegetables" style="background:linear-gradient(135deg,#eeeae2,#c9734a 50%,#5d7a3a)"></div>
  <h3 class="name">The Ashcombe <span class="rating"><i></i><i></i><i></i><i class="off"></i><i class="off"></i></span></h3>
  <p class="meta" style="top:27px"><svg><use href="#i-phone"/></svg>+44 (0)20 7946 0581, 0871 4600 217<span class="gap"></span><svg><use href="#i-web"/></svg>Website<span class="gap"></span><svg><use href="#i-mail"/></svg>E-mail</p>
  <p class="meta" style="top:48px;white-space:normal;width:280px;align-items:flex-start;line-height:10px"><svg><use href="#i-pin"/></svg>63 Ashcombe Rd, London W11 5JN, England (Bayswater / Notting Hill / Lancaster Gate )</p>
  <p class="meta" style="top:78px"><svg><use href="#i-fork"/></svg>European, French</p>
  <p class="meta" style="top:98px"><svg><use href="#i-bag"/></svg>£70 - £94</p>
</article>

<aside>
  <section class="abs widget" style="top:450px">
    <h3>CATEGORIES</h3>
    <ul>
      <li><span class="cb"><svg><use href="#i-tick"/></svg></span>All (114)</li>
      <li><span class="cb"></span>African (0)</li>
      <li><span class="cb"></span>American (5)</li>
      <li><span class="cb"></span>Asian (2)</li>
      <li><span class="cb"></span>Bakery (0)</li>
    </ul>
    <a class="more">more...</a>
  </section>
  <section class="abs widget" style="top:608px">
    <h3>LOCATION</h3>
    <ul>
      <li><span class="cb"><svg><use href="#i-tick"/></svg></span>All (300)</li>
      <li><span class="cb"></span>Bayswater / Notting Hill (134)</li>
      <li><span class="cb"></span>Bloomsbury / Holborn (206)</li>
      <li><span class="cb"></span>Camden / Primrose Hill (65)</li>
      <li><span class="cb"></span>Charing Cross / Trafalgar Square (79)</li>
    </ul>
    <a class="more">more...</a>
  </section>
  <section class="abs widget" style="top:766px">
    <h3>PRICES</h3>
    <ul>
      <li><span class="cb"></span>All (650)</li>
      <li><span class="cb"><svg><use href="#i-tick"/></svg></span>$ (100)</li>
      <li><span class="cb"></span>$$ (200)</li>
      <li><span class="cb"></span>$$$ (150)</li>
      <li><span class="cb"></span>$$$$ (100)</li>
    </ul>
  </section>
</aside>

<footer>
  <div class="abs footer-line"></div>
  <section class="abs newest">
    <h4 class="foot-h">Newest restaurants</h4>
    <ul>
      <li>Restaurant Marcus Ellery</li>
      <li>The Linden Rooms</li>
      <li>Quince</li>
      <li>The Copper Kettle Restaurant &amp; Bar</li>
      <li>Bella Rosa Cafe &amp; Restaurant</li>
    </ul>
  </section>
  <section class="abs tweets">
    <h4 class="foot-h">Latest tweets</h4>
    <div class="list">
      <p class="tweet">Lorem ipsum dolor sit amet, consectetur adipiscing elit.<br>Bonum valitudo: miser morbus. Paria sunt igitur.</p>
      <p class="tweet">Sed haec omittamus; Pauca mutat vel plura sane; Ita fit<br>cum gravior, tum etiam splendidior oratio.</p>
      <p class="tweet">Eam tum adesse, cum dolor omnis absit;</p>
      <p class="tweet">Quid ergo hoc loco intellegit honestum.</p>
    </div>
  </section>
  <nav class="abs social">
    <span class="first">Friendlo</span><span>Chirpa</span><span>Gloop</span><span>Pinora</span>
  </nav>
  <p class="abs copy">Copyright © Zestmora London 2013.<br>All rights reserved.</p>
</footer>
</body>
</html>
```